Custom hot rod builder needs a website for launch of new business where he will build luxury garages

We need a website that gives a WOW first impression for "Vantor Hangars". This is a new business so photos are renderings but we need it to really attract a particular audience. Our initial business is custom hot rods so now we are building garages for them. These will be like luxury "homes" for cars! I will attach our new logo. Website needs to feel powerful and prestigious.

Target Market(s)

middle aged men, car enthusiasts

Industry/Entity Type

automotive, construction

Number of Pages Required

2 page

Font styles to use
Serif

Colors
0054AA
0677BA
7BADD7
CADEEF
E8F1F8

Requirements
Must have
• a WOW factor. luxury. contact form.
Nice to have
• ?

```html
<!DOCTYPE html>
<html lang="en">
<head>
<meta charset="utf-8">
<title>Vantor Hangars</title>
<link href="https://fonts.googleapis.com/css2?family=DM+Serif+Display&family=Inter:wght@400;500;600&display=swap" rel="stylesheet">
<style>
:root{
  --accent:#27a8e0;
  --accent-dark:#0677ba;
  --ink:#141414;
  --body:#333;
  --muted:#666;
  --panel:#f2f2f2;
  --band:#f4f4f4;
  --white:#fff;
  --line:#d6dde4;
  --avatar:#8aa9cf;
  --star:#f2b01e;
}
*{margin:0;padding:0;box-sizing:border-box}
html,body{width:1200px;height:5312px;overflow:hidden}
body{position:relative;background:var(--white);font-family:"Inter",Arial,sans-serif;color:var(--body)}
.serif{font-family:"DM Serif Display",Georgia,serif;font-weight:400}
section,header,footer{position:absolute;left:0;width:1200px}
.photo{position:absolute}
.btn{display:inline-flex;align-items:center;justify-content:center;background:var(--accent);color:var(--white);font-family:inherit;font-size:13px;font-weight:600;border:0;border-radius:4px;text-decoration:none}
.eyebrow{font-size:14px;letter-spacing:1.5px;color:var(--accent);text-transform:uppercase}
.section-head{position:absolute;left:0;width:1200px;text-align:center}
.section-head h2{font-family:"DM Serif Display",Georgia,serif;font-weight:400;font-size:42px;color:var(--ink);margin-top:6px}

/* header */
.topbar{top:0;height:88px;background:var(--white);z-index:3}
.brand{position:absolute;left:36px;top:28px;display:flex;align-items:center;gap:8px;font-family:"DM Serif Display",Georgia,serif;font-size:22px;color:var(--accent)}
.brand-dot{width:24px;height:24px;border-radius:50%;background:var(--accent)}
.nav{position:absolute;right:40px;top:30px;display:flex;gap:28px;font-size:14px;font-weight:500}
.nav a{color:var(--ink);text-decoration:none}
.nav a.active{color:var(--accent)}

/* hero */
.hero{top:88px;height:584px}
.hero .photo{inset:0;background:linear-gradient(100deg,#5a4a1e 0%,#3b3524 35%,#2a2f38 65%,#4a4f58 100%)}
.hero .shade{position:absolute;inset:0;background:rgba(10,15,25,.45)}
.hero-copy{position:absolute;left:0;top:112px;width:1200px;text-align:center;color:var(--white)}
.hero-copy h1{font-family:"DM Serif Display",Georgia,serif;font-weight:400;font-size:64px;line-height:1.12;width:760px;margin:0 auto}
.hero-copy p{font-size:17px;line-height:1.5;width:580px;margin:28px auto 0}
.hero-copy .btn{margin-top:56px;width:232px;height:50px}

/* about */
.about{top:672px;height:776px}
.about-panel{position:absolute;left:100px;top:48px;width:520px;height:680px;background:var(--panel);padding:74px 56px 0}
.about-panel h2{font-size:42px;color:var(--ink);margin:6px 0 26px}
.about-panel p{font-size:16px;line-height:1.6;width:380px}
.about-panel .btn{margin-top:34px;width:232px;height:50px}
.about .photo{left:520px;top:120px;width:640px;height:560px;background:linear-gradient(135deg,#b8b2a6,#5e5a54 55%,#2b2b2d);clip-path:polygon(14% 0,100% 0,100% 100%,0 100%)}

/* services */
.services{top:1448px;height:852px;background:var(--band)}
.services .section-head{top:100px}
.cards{position:absolute;top:244px;left:104px;display:flex;gap:100px}
.service-card{width:264px;height:504px;background:var(--white);box-shadow:0 2px 8px rgba(0,0,0,.06)}
.service-card .photo{position:relative;height:190px;background:linear-gradient(135deg,#6d5a45,#2c2621)}
.service-card:nth-child(2) .photo{background:linear-gradient(135deg,#9aa0a6,#2d3034)}
.service-card:nth-child(3) .photo{background:linear-gradient(135deg,#8a7a66,#3a3530)}
.service-card h3{font-size:30px;color:var(--ink);text-align:center;margin:28px 0 14px}
.service-card p{font-size:16px;line-height:1.55;text-align:center;padding:0 20px;color:var(--ink)}
.service-card .btn{display:flex;width:200px;height:46px;margin:28px auto 0}

/* why us */
.why{top:2300px;height:900px}
.why .section-head{top:100px}
.why .photo{left:208px;top:240px;width:384px;height:568px;background:linear-gradient(135deg,#4b5866,#1f252c 60%,#3a3126)}
.reasons{position:absolute;left:632px;top:240px;width:468px}
.reason{height:124px;background:var(--panel);border-radius:62px;margin-bottom:24px;padding:34px 0 0 34px}
.reason h3{font-size:22px;color:var(--ink)}
.reason p{font-size:13px;color:var(--body);margin-top:12px}

/* news */
.news{top:3200px;height:760px;background:var(--band)}
.news .section-head{top:96px}
.news-row{position:absolute;top:248px;left:100px;display:flex;gap:32px}
.news-item{display:flex;gap:16px;height:412px}
.news-item .photo{position:relative;width:244px;height:412px;background:linear-gradient(135deg,#7b6a55,#2f2a25)}
.news-item:nth-child(2) .photo{background:linear-gradient(135deg,#c9c7c2,#4a4c50)}
.news-text{width:224px;background:var(--white);padding:26px 16px 0}
.news-text h3{font-family:"Inter",Arial,sans-serif;font-size:14px;font-weight:500;line-height:1.45;color:var(--accent)}
.news-text p{font-size:11px;line-height:1.6;color:var(--muted);margin-top:16px}

/* testimonials */
.testimonials{top:3960px;height:680px}
.testimonials .section-head{top:96px}
.quotes{position:absolute;top:240px;left:104px;display:flex;gap:20px}
.quote{width:488px;height:228px;background:var(--panel);padding:34px 28px}
.quote-top{display:flex;align-items:center;gap:26px}
.avatar{width:64px;height:64px;border-radius:50%;background:var(--avatar);color:var(--white);display:flex;align-items:center;justify-content:center;font-size:22px;font-weight:600}
.quote h3{font-size:22px;color:var(--ink)}
.stars{display:flex;margin-top:4px}
.quote p{font-size:15px;line-height:1.55;margin:22px 0 0 90px;color:var(--body)}
.testimonials .more{position:absolute;left:484px;top:524px;width:232px;height:52px}

/* booking */
.booking{top:4640px;left:60px;width:1080px;height:160px;background:var(--white);border-radius:14px;box-shadow:0 4px 20px rgba(0,0,0,.12);z-index:2}
.booking h2{position:absolute;left:64px;top:54px;font-size:38px;color:var(--ink);white-space:nowrap}
.booking-form{position:absolute;left:460px;top:56px;display:flex;gap:12px}
.booking-form input{width:150px;height:50px;border:1px solid var(--line);border-radius:4px;padding:0 14px;font-family:inherit;font-size:13px;color:var(--body);background:var(--white)}
.booking-form .btn{width:232px;height:50px;margin-left:2px}

/* footer */
.footer{top:4740px;height:572px;background:var(--accent);color:var(--white)}
.footer h3{font-size:30px;color:var(--white)}
.col{position:absolute;top:132px}
.col-brand{left:104px;width:300px}
.col-brand p{font-size:15px;line-height:1.6;margin-top:26px;opacity:.95}
.col-links{left:504px}
.col-links ul{list-style:none;margin-top:24px}
.col-links li{font-size:16px;line-height:1.75}
.col-contact{left:792px}
.contact-list{list-style:none;margin-top:40px}
.contact-list li{display:flex;align-items:center;gap:22px;font-size:15px;margin-bottom:30px}
.icon{width:30px;height:30px;border-radius:50%;background:var(--white);display:flex;align-items:center;justify-content:center}
.footer .rule{position:absolute;left:0;top:462px;width:1200px;height:1px;background:rgba(255,255,255,.45)}
.copyright{position:absolute;left:0;top:500px;width:1200px;text-align:center;font-size:12px}
</style>
</head>
<body>

<header class="topbar">
  <div class="brand"><span class="brand-dot"></span>VANTOR</div>
  <nav class="nav">
    <a class="active" href="#">Home</a><a href="#">About Us</a><a href="#">Services</a><a href="#">News</a><a href="#">Testimonials</a><a href="#">Contact Us</a>
  </nav>
</header>

<section class="hero">
  <div class="photo" role="img" aria-label="Rendering of a custom hot rod inside a luxury private hangar"></div>
  <div class="shade"></div>
  <div class="hero-copy">
    <h1>Give Your Car A true Custom Look</h1>
    <p>Luxury hangars built by hot rod craftsmen. A private, climate-controlled home worthy of your machine.</p>
    <a class="btn" href="#contact">Contact Us</a>
  </div>
</section>

<section class="about">
  <div class="about-panel">
    <div class="eyebrow">About Us</div>
    <h2 class="serif">Who We Are</h2>
    <p>We started in the shop, building custom hot rods by hand. Now we build the homes they deserve. Every Vantor hangar is designed around the car inside it: heated floors, gallery lighting, lift bays and a lounge to admire your collection. Built with the same care, precision and pride we put into every build that rolls out of our doors.</p>
    <a class="btn" href="#">Read More</a>
  </div>
  <div class="photo" role="img" aria-label="Rendering of a polished hot rod under gallery lighting in a hangar"></div>
</section>

<section class="services">
  <div class="section-head"><div class="eyebrow">Services</div><h2>What We Offer</h2></div>
  <div class="cards">
    <article class="service-card">
      <div class="photo" role="img" aria-label="Hangar interior finishes and materials"></div>
      <h3 class="serif">Multiple Options</h3>
      <p>Single-bay retreats to full collector halls, each tailored to your cars and your land.</p>
      <a class="btn" href="#">Read More</a>
    </article>
    <article class="service-card">
      <div class="photo" role="img" aria-label="Hangar structure being assembled on site"></div>
      <h3 class="serif">Deliver &amp; Install</h3>
      <p>Our crew handles design, permits and build so your hangar arrives turnkey.</p>
      <a class="btn" href="#">Read More</a>
    </article>
    <article class="service-card">
      <div class="photo" role="img" aria-label="Builder working on a custom hot rod"></div>
      <h3 class="serif">Service &amp; Repair</h3>
      <p>Custom hot rod builds and restoration from the team that started it all.</p>
      <a class="btn" href="#">Read More</a>
    </article>
  </div>
</section>

<section class="why">
  <div class="section-head"><div class="eyebrow">Advantages</div><h2>Why Choose Us</h2></div>
  <div class="photo" role="img" aria-label="Craftsman working on an engine in the build shop"></div>
  <div class="reasons">
    <div class="reason"><h3 class="serif">Fast Low Cost Foreign</h3><p>Efficient builds with premium materials sourced worldwide</p></div>
    <div class="reason"><h3 class="serif">Customer Services</h3><p>One dedicated builder guides you from sketch to keys</p></div>
    <div class="reason"><h3 class="serif">Largest Range</h3><p>Lifts, lounges, showroom glass and detailing bays</p></div>
    <div class="reason"><h3 class="serif">Reasonable</h3><p>Clear, fixed pricing with no surprises along the way</p></div>
  </div>
</section>

<section class="news">
  <div class="section-head"><div class="eyebrow">News</div><h2>Latest News &amp; Articles</h2></div>
  <div class="news-row">
    <article class="news-item">
      <div class="photo" role="img" aria-label="Hands fitting a chrome engine part"></div>
      <div class="news-text">
        <h3>Why your hot rod deserves more than a standard garage: climate, light and security explained.</h3>
        <p>Humidity, dust and temperature swings slowly wear on paint, leather and chrome. A purpose-built hangar keeps conditions steady all year. We look at insulation, ventilation, floor coatings and lighting, and how each one protects the value of the cars you have spent years building and collecting.</p>
      </div>
    </article>
    <article class="news-item">
      <div class="photo" role="img" aria-label="Rendering of a hangar exterior at dusk"></div>
      <div class="news-text">
        <h3>Inside our first luxury hangar: a showroom, lounge and workshop under one roof.</h3>
        <p>Our launch build pairs a six-car gallery with a mezzanine lounge and a fully equipped service bay. Floor-to-ceiling glass puts the collection on display, while hidden storage keeps tools out of sight. Here is how the design came together, from the first sketch on the shop bench to the finished space.</p>
      </div>
    </article>
  </div>
</section>

<section class="testimonials">
  <div class="section-head"><div class="eyebrow">Testimonials</div><h2>What Our Client Say About Us</h2></div>
  <div class="quotes">
    <div class="quote">
      <div class="quote-top"><div class="avatar">D</div><div><h3 class="serif">Dana R</h3>
        <div class="stars"><svg width="90" height="16" viewBox="0 0 90 16"><g fill="#f2b01e"><path id="st" d="M8 0l2.4 5.2 5.6.6-4.2 3.8 1.2 5.6L8 12.4 3 15.2l1.2-5.6L0 5.8l5.6-.6z"/><use href="#st" x="18"/><use href="#st" x="36"/><use href="#st" x="54"/><use href="#st" x="72"/></g></svg></div></div></div>
      <p>They built my coupe years ago and now its hangar. Both are flawless, and I love spending evenings there.</p>
    </div>
    <div class="quote">
      <div class="quote-top"><div class="avatar">T</div><div><h3 class="serif">Tom K</h3>
        <div class="stars"><svg width="90" height="16" viewBox="0 0 90 16"><g fill="#f2b01e"><use href="#st"/><use href="#st" x="18"/><use href="#st" x="36"/><use href="#st" x="54"/><use href="#st" x="72"/></g></svg></div></div></div>
      <p>The gallery lighting and lounge turned my garage into a showroom. Every visitor asks who built it.</p>
    </div>
  </div>
  <a class="btn more" href="#">Read More</a>
</section>

<section class="booking" id="contact">
  <h2 class="serif">Book An Appointment</h2>
  <form class="booking-form" action="#" method="post">
    <input type="text" name="name" placeholder="Your name" aria-label="Your name">
    <input type="email" name="email" placeholder="Email" aria-label="Email">
    <button class="btn" type="submit">Contact us</button>
  </form>
</section>

<footer class="footer">
  <div class="col col-brand">
    <h3 class="serif">Vantor Hangars</h3>
    <p>Custom hot rod builders creating luxury hangars for the cars we love. Designed, built and finished by hand, with the same pride as every build we deliver.</p>
  </div>
  <div class="col col-links">
    <h3 class="serif">Quick Links</h3>
    <ul><li>Home</li><li>About Us</li><li>Services</li><li>News</li><li>Testimonials</li><li>Contact Us</li></ul>
  </div>
  <div class="col col-contact">
    <h3 class="serif">Contact Info</h3>
    <ul class="contact-list">
      <li><span class="icon"><svg width="14" height="14" viewBox="0 0 24 24"><path fill="#27a8e0" d="M6.6 10.8a15 15 0 0 0 6.6 6.6l2.2-2.2c.3-.3.7-.4 1-.2 1.1.4 2.3.6 3.6.6.6 0 1 .4 1 1V20c0 .6-.4 1-1 1A17 17 0 0 1 3 4c0-.6.4-1 1-1h3.5c.6 0 1 .4 1 1 0 1.3.2 2.5.6 3.6.1.3 0 .7-.2 1z"/></svg></span>(555) 014-2280</li>
      <li><span class="icon"><svg width="14" height="14" viewBox="0 0 24 24"><path fill="#27a8e0" d="M12 2a7 7 0 0 0-7 7c0 5.2 7 13 7 13s7-7.8 7-13a7 7 0 0 0-7-7zm0 9.5A2.5 2.5 0 1 1 12 6.5a2.5 2.5 0 0 1 0 5z"/></svg></span>48 Ridgeline Way, Harwell</li>
      <li><span class="icon"><svg width="14" height="14" viewBox="0 0 24 24"><path fill="#27a8e0" d="M3 5h18v14H3zm2 2v.5l7 4.5 7-4.5V7l-7 4.5z"/></svg></span>hello@vantorhangars.example</li>
    </ul>
  </div>
  <div class="rule"></div>
  <div class="copyright">© 2024 Vantor Hangars. ALL RIGHTS RESERVED</div>
</footer>

</body>
</html>
```